Speisekarten für ein modernes, junges Café
Zielgruppe
Wir suchen eine Speisekarte für ein modernes, junges Café. Frühstück, kleine Speisen, Snacks und Getränke stehen auf der Karte. Unsere Zielgruppe sind hauptsächlich junge Menschen bis 40 Jahre.
Die Speisekarte sollte immer änderbar sein ( nur Text bei neuen Speisen zum Beispiel )
Aufgabenstellung
Das Logo kann und soll gerne mit eingefügt werden. Eventuell gleich auf dem Deckblatt.
Generell bin ich offen für junge, coole Ideen.
Unten die Themen/ grobe Überschriften
Kaffee und Espresso
Frühstücksvariationen
Eierspeisen
Frühstück zum löffeln
Pancakes
Extras zum Frühstück
Snacks/ kleine Speisen
-die Kurbel. Drinks
-die Kurbel. Wein & Bier )
((Kinderspeisekarte:
zusätzlich noch ein extra Blatt für die Kinder zum ausmalen mit den illustrierten Bildern auch im modernen Stil ))

```html
<!DOCTYPE html>
<html lang="de">
<head>
<meta charset="utf-8">
<title>die Kurbel. – Speisekarten</title>
<link href="https://fonts.googleapis.com/css2?family=Quicksand:wght@500;600;700&family=Poppins:wght@400;600&display=swap" rel="stylesheet">
<style>
  :root{
    --ink:#2b2a29;
    --tan:#d3b99b;
    --tan-text:#dcc2a1;
    --paper:#ffffff;
    --grey-text:#2b2a29;
    --rule:#8a7d6e;
  }
  *{margin:0;padding:0;box-sizing:border-box}
  html,body{width:1200px;height:834px;overflow:hidden;background:var(--paper)}
  body{position:relative;font-family:"Quicksand",sans-serif}
  .sheet{position:absolute;overflow:hidden;box-shadow:6px 8px 14px rgba(0,0,0,.18)}
  .abs{position:absolute}
  .center-x{left:0;right:0;text-align:center}

  /* Full A4 pages */
  .page{width:291px;height:411px;background:var(--ink)}
  .page-band{position:absolute;left:0;top:0;width:100%;background:var(--tan)}
  .brand-seal{position:absolute;border-radius:50%;background:var(--ink);border:2px solid var(--paper);
    display:flex;align-items:center;justify-content:center;color:var(--tan-text);font-family:"Quicksand",sans-serif;font-weight:700}
  .page-title{color:var(--paper);font-weight:500;font-size:15px;letter-spacing:.4px;line-height:1.15}
  .page-sub{color:var(--tan-text);font-weight:500;font-size:14px;letter-spacing:.4px}
  .section-title{color:var(--tan-text);font-weight:500;font-size:10px;letter-spacing:.3px;text-align:center}
  .icon-slot{position:absolute;background:linear-gradient(135deg,#6b5f52,#a89176);border-radius:6px;opacity:.55}
  .col{position:absolute;width:115px}
  .item{height:35px}
  .item-name{color:var(--tan-text);font-weight:600;font-size:8.6px;white-space:nowrap;letter-spacing:.1px}
  .item-desc{color:var(--paper);font-family:"Poppins",sans-serif;font-size:5.4px;line-height:1.5;margin-top:2px;letter-spacing:-.1px}

  /* Folded menus */
  .fold{height:272px}
  .panel{position:absolute;top:0;width:129px;height:272px;overflow:hidden}
  .panel-tan{background:var(--tan)}
  .panel-white{background:linear-gradient(90deg,#ffffff 70%,#e9e9e9)}
  .panel-dark{background:var(--ink)}
  .panel-tan::after{content:"";position:absolute;right:0;top:0;width:10px;height:100%;background:linear-gradient(90deg,rgba(0,0,0,0),rgba(0,0,0,.12))}
  .mini-head{font-weight:700;font-size:6.6px;text-align:center;letter-spacing:.2px}
  .on-tan .mini-head,.on-dark .mini-head{color:var(--paper)}
  .on-white .mini-head{color:var(--ink)}
  .mini-col{position:absolute;left:22px;width:95px}
  .mini-item{position:absolute;left:0}
  .mini-name{font-weight:600;font-size:6px;white-space:nowrap}
  .mini-desc{font-family:"Poppins",sans-serif;font-size:4.2px;line-height:1.55;margin-top:1px;letter-spacing:-.1px}
  .on-tan .mini-name{color:var(--paper)} .on-tan .mini-desc{color:var(--ink)}
  .on-white .mini-name{color:var(--tan)} .on-white .mini-desc{color:var(--ink)}
  .on-dark .mini-name{color:var(--tan-text)} .on-dark .mini-desc{color:var(--paper)}
  .mini-icon{position:absolute;left:50%;width:22px;height:13px;margin-left:-11px;border-radius:5px;opacity:.6}
  .on-tan .mini-icon{background:linear-gradient(135deg,#fff,#e9dccb)}
  .on-white .mini-icon,.on-dark .mini-icon{background:linear-gradient(135deg,#8f8a84,#4a4744)}
  .on-dark .mini-icon{background:linear-gradient(135deg,#d8c3a8,#8c7a66)}
  .mini-rule{position:absolute;left:11px;right:11px;height:0;border-top:.6px solid var(--rule)}
  .on-white .mini-rule{border-color:#444}

  /* Kids */
  .kids-cover{left:862px;top:517px;width:137px;height:290px;background:var(--ink)}
  .kids-inside{left:1025px;top:517px;width:138px;height:291px;background:var(--paper)}
</style>
</head>
<body>

<!-- Coffee & Breakfast cover page -->
<section class="sheet page" style="left:117px;top:50px">
  <div class="page-band" style="height:60px"></div>
  <div class="brand-seal" style="left:102px;top:15px;width:86px;height:86px;font-size:13px">die Kurbel.</div>
  <h1 class="abs center-x page-title" style="top:115px">Coffe &amp; Breakfast</h1>
  <p class="abs center-x page-sub" style="top:134px">- Menu -</p>

  <div class="icon-slot" role="img" aria-label="Kaffeetasse mit Dampf, Strichzeichnung" style="left:57px;top:170px;width:24px;height:26px"></div>
  <div class="icon-slot" role="img" aria-label="Frühstücksteller mit Spiegelei, Strichzeichnung" style="left:185px;top:178px;width:42px;height:18px"></div>
  <h2 class="abs section-title" style="left:10px;width:125px;top:208px">Kaffee &amp; Espresso</h2>
  <h2 class="abs section-title" style="left:148px;width:130px;top:208px">Frühstücksvariationen</h2>

  <div class="col" style="left:26px;top:237px">
    <div class="item"><p class="item-name">Name of drink ................15$</p><p class="item-desc">Nulla tempus justo in nunc eleifend,<br>nec sagittis nunc imperdiet.</p></div>
    <div class="item"><p class="item-name">Name of drink ................ 9$</p><p class="item-desc">Nulla tempus justo in nunc eleifend,<br>nec sagittis nunc imperdiet.</p></div>
    <div class="item"><p class="item-name">Name of drink ................12$</p><p class="item-desc">Nulla tempus justo in nunc eleifend,<br>nec sagittis nunc imperdiet.</p></div>
    <div class="item"><p class="item-name">Name of drink ................11$</p><p class="item-desc">Nulla tempus justo in nunc eleifend,<br>nec sagittis nunc imperdiet.</p></div>
  </div>
  <div class="col" style="left:157px;top:237px">
    <div class="item"><p class="item-name">Name of dish................15$</p><p class="item-desc">Nulla tempus justo in nunc eleifend,<br>nec sagittis nunc imperdiet.</p></div>
    <div class="item"><p class="item-name">Name of dish................ 9$</p><p class="item-desc">Nulla tempus justo in nunc eleifend,<br>nec sagittis nunc imperdiet.</p></div>
    <div class="item"><p class="item-name">Name of dish................12$</p><p class="item-desc">Nulla tempus justo in nunc eleifend,<br>nec sagittis nunc imperdiet.</p></div>
    <div class="item"><p class="item-name">Name of dish................11$</p><p class="item-desc">Nulla tempus justo in nunc eleifend,<br>nec sagittis nunc imperdiet.</p></div>
  </div>
</section>

<!-- Eggs & Breakfast page -->
<section class="sheet page" style="left:438px;top:50px">
  <div class="page-band" style="height:38px"></div>
  <div class="brand-seal" style="left:115px;top:8px;width:60px;height:60px;font-size:9.5px">die Kurbel.</div>
  <h1 class="abs center-x page-title" style="top:81px">Eggs &amp; Breakfast</h1>
  <p class="abs center-x page-sub" style="top:98px">- Menu -</p>
  <div class="icon-slot" role="img" aria-label="Henne im Nest, Strichzeichnung" style="left:60px;top:138px;width:36px;height:32px"></div>
  <div class="icon-slot" role="img" aria-label="Schüssel mit Kanne, Strichzeichnung" style="left:197px;top:138px;width:34px;height:32px"></div>
  <h2 class="abs section-title" style="left:10px;width:135px;top:179px">Eierspeisen</h2>
  <h2 class="abs section-title" style="left:148px;width:135px;top:179px">Frühstück zum löffeln</h2>
  <div class="col" style="left:30px;top:208px">
    <div class="item"><p class="item-name">Name of dish................15$</p><p class="item-desc">Nulla tempus justo in nunc eleifend,<br>nec sagittis nunc imperdiet.</p></div>
    <div class="item"><p class="item-name">Name of dish................ 9$</p><p class="item-desc">Nulla tempus justo in nunc eleifend,<br>nec sagittis nunc imperdiet.</p></div>
    <div class="item"><p class="item-name">Name of dish................12$</p><p class="item-desc">Nulla tempus justo in nunc eleifend,<br>nec sagittis nunc imperdiet.</p></div>
    <div class="item" style="height:38px"><p class="item-name">Name of dish................11$</p><p class="item-desc">Nulla tempus justo in nunc eleifend,<br>nec sagittis nunc imperdiet.</p></div>
    <div class="item"><p class="item-name">Name of dish................11$</p><p class="item-desc">Nulla tempus justo in nunc eleifend,<br>nec sagittis nunc imperdiet.</p></div>
  </div>
  <div class="col" style="left:161px;top:208px">
    <div class="item"><p class="item-name">Name of dish................15$</p><p class="item-desc">Nulla tempus justo in nunc eleifend,<br>nec sagittis nunc imperdiet.</p></div>
    <div class="item"><p class="item-name">Name of dish................ 9$</p><p class="item-desc">Nulla tempus justo in nunc eleifend,<br>nec sagittis nunc imperdiet.</p></div>
    <div class="item"><p class="item-name">Name of dish................12$</p><p class="item-desc">Nulla tempus justo in nunc eleifend,<br>nec sagittis nunc imperdiet.</p></div>
    <div class="item" style="height:38px"><p class="item-name">Name of dish................11$</p><p class="item-desc">Nulla tempus justo in nunc eleifend,<br>nec sagittis nunc imperdiet.</p></div>
    <div class="item"><p class="item-name">Name of dish................11$</p><p class="item-desc">Nulla tempus justo in nunc eleifend,<br>nec sagittis nunc imperdiet.</p></div>
  </div>
</section>

<!-- Pancakes & Extras page -->
<section class="sheet page" style="left:763px;top:50px">
  <div class="page-band" style="height:38px"></div>
  <div class="brand-seal" style="left:115px;top:8px;width:60px;height:60px;font-size:9.5px">die Kurbel.</div>
  <h1 class="abs center-x page-title" style="top:81px">Pancakes &amp; Extras</h1>
  <p class="abs center-x page-sub" style="top:98px">- Menu -</p>
  <div class="icon-slot" role="img" aria-label="Pancake-Stapel, Strichzeichnung" style="left:56px;top:152px;width:42px;height:16px"></div>
  <div class="icon-slot" role="img" aria-label="Brotkorb, Strichzeichnung" style="left:196px;top:140px;width:36px;height:30px"></div>
  <h2 class="abs section-title" style="left:10px;width:130px;top:179px">Pancakes</h2>
  <h2 class="abs section-title" style="left:148px;width:135px;top:179px">Extras zum Frühstück</h2>
  <div class="col" style="left:30px;top:208px">
    <div class="item"><p class="item-name">Name of dish................15$</p><p class="item-desc">Nulla tempus justo in nunc eleifend,<br>nec sagittis nunc imperdiet.</p></div>
    <div class="item"><p class="item-name">Name of dish................ 9$</p><p class="item-desc">Nulla tempus justo in nunc eleifend,<br>nec sagittis nunc imperdiet.</p></div>
    <div class="item"><p class="item-name">Name of dish................12$</p><p class="item-desc">Nulla tempus justo in nunc eleifend,<br>nec sagittis nunc imperdiet.</p></div>
    <div class="item" style="height:38px"><p class="item-name">Name of dish................11$</p><p class="item-desc">Nulla tempus justo in nunc eleifend,<br>nec sagittis nunc imperdiet.</p></div>
    <div class="item"><p class="item-name">Name of dish................11$</p><p class="item-desc">Nulla tempus justo in nunc eleifend,<br>nec sagittis nunc imperdiet.</p></div>
  </div>
  <div class="col" style="left:161px;top:208px">
    <div class="item"><p class="item-name">Name of dish................15$</p><p class="item-desc">Nulla tempus justo in nunc eleifend,<br>nec sagittis nunc imperdiet.</p></div>
    <div class="item"><p class="item-name">Name of dish................ 9$</p><p class="item-desc">Nulla tempus justo in nunc eleifend,<br>nec sagittis nunc imperdiet.</p></div>
    <div class="item"><p class="item-name">Name of dish................12$</p><p class="item-desc">Nulla tempus justo in nunc eleifend,<br>nec sagittis nunc imperdiet.</p></div>
    <div class="item" style="height:38px"><p class="item-name">Name of dish................11$</p><p class="item-desc">Nulla tempus justo in nunc eleifend,<br>nec sagittis nunc imperdiet.</p></div>
    <div class="item"><p class="item-name">Name of dish................11$</p><p class="item-desc">Nulla tempus justo in nunc eleifend,<br>nec sagittis nunc imperdiet.</p></div>
  </div>
</section>

<!-- Trifold, outside -->
<section class="sheet fold" style="left:29px;top:531px;width:387px">
  <div class="panel panel-tan on-tan" style="left:0">
    <h3 class="abs center-x mini-head" style="top:11px">Pancakes</h3>
    <div class="mini-icon" role="img" aria-label="Pancake-Teller, Strichzeichnung" style="top:25px"></div>
    <div class="mini-col" style="top:0;height:272px">
      <div class="mini-item" style="top:49px"><p class="mini-name">Name of dish................15$</p><p class="mini-desc">Nulla tempus justo in nunc eleifend,<br>nec sagittis nunc imperdiet.</p></div>
      <div class="mini-item" style="top:81px"><p class="mini-name">Name of dish................ 9$</p><p class="mini-desc">Nulla tempus justo in nunc eleifend,<br>nec sagittis nunc imperdiet.</p></div>
      <div class="mini-item" style="top:112px"><p class="mini-name">Name of dish................12$</p><p class="mini-desc">Nulla tempus justo in nunc eleifend,<br>nec sagittis nunc imperdiet.</p></div>
      <div class="mini-item" style="top:194px"><p class="mini-name">Name of dish................ 9$</p><p class="mini-desc">Nulla tempus justo in nunc eleifend,<br>nec sagittis nunc imperdiet.</p></div>
      <div class="mini-item" style="top:225px"><p class="mini-name">Name of dish................12$</p><p class="mini-desc">Nulla tempus justo in nunc eleifend,<br>nec sagittis nunc imperdiet.</p></div>
    </div>
    <div class="mini-rule" style="top:142px;border-color:#fff"></div>
    <h3 class="abs center-x mini-head" style="top:150px">Extras zum Frühstück</h3>
    <div class="mini-icon" role="img" aria-label="Brotkorb, Strichzeichnung" style="top:166px;width:20px;height:18px;margin-left:-10px"></div>
  </div>
  <div class="panel panel-white on-white" style="left:129px">
    <div class="mini-col" style="left:24px;top:0;height:272px">
      <div class="mini-item" style="top:16px"><p class="mini-name">Name of dish................15$</p><p class="mini-desc">Nulla tempus justo in nunc eleifend,<br>nec sagittis nunc imperdiet.</p></div>
      <div class="mini-item" style="top:48px"><p class="mini-name">Name of dish................15$</p><p class="mini-desc">Nulla tempus justo in nunc eleifend,<br>nec sagittis nunc imperdiet.</p></div>
      <div class="mini-item" style="top:80px"><p class="mini-name">Name of dish................15$</p><p class="mini-desc">Nulla tempus justo in nunc eleifend,<br>nec sagittis nunc imperdiet.</p></div>
      <div class="mini-item" style="top:160px"><p class="mini-name">Name of dish................15$</p><p class="mini-desc">Nulla tempus justo in nunc eleifend,<br>nec sagittis nunc imperdiet.</p></div>
      <div class="mini-item" style="top:192px"><p class="mini-name">Name of dish................15$</p><p class="mini-desc">Nulla tempus justo in nunc eleifend,<br>nec sagittis nunc imperdiet.</p></div>
      <div class="mini-item" style="top:223px"><p class="mini-name">Name of dish................15$</p><p class="mini-desc">Nulla tempus justo in nunc eleifend,<br>nec sagittis nunc imperdiet.</p></div>
    </div>
    <div class="mini-rule" style="top:110px"></div>
    <h3 class="abs center-x mini-head" style="top:118px">Snacks &amp; kleine Speisen</h3>
    <div class="mini-icon" role="img" aria-label="Schale und Baguette, Strichzeichnung" style="top:132px;width:44px;margin-left:-22px"></div>
  </div>
  <div class="panel panel-dark on-dark" style="left:258px">
    <div class="brand-seal" style="left:22px;top:49px;width:84px;height:84px;font-size:13px">die Kurbel.</div>
    <p class="abs center-x page-title" style="top:151px;font-size:11.5px">Coffe &amp; Breakfast</p>
    <p class="abs center-x page-sub" style="top:165px;font-size:11px">- Menu -</p>
  </div>
</section>

<!-- Trifold, inside -->
<section class="sheet fold" style="left:441px;top:531px;width:386px">
  <div class="panel panel-tan on-tan" style="left:0">
    <h3 class="abs center-x mini-head" style="top:11px">Kaffee &amp; Espresso</h3>
    <div class="mini-icon" role="img" aria-label="Kaffeetasse, Strichzeichnung" style="top:25px;width:14px;height:15px;margin-left:-7px"></div>
    <div class="mini-col" style="top:0;height:272px">
      <div class="mini-item" style="top:54px"><p class="mini-name">Name of drink ...............15$</p><p class="mini-desc">Nulla tempus justo in nunc eleifend,<br>nec sagittis nunc imperdiet.</p></div>
      <div class="mini-item" style="top:86px"><p class="mini-name">Name of drink ............... 9$</p><p class="mini-desc">Nulla tempus justo in nunc eleifend,<br>nec sagittis nunc imperdiet.</p></div>
      <div class="mini-item" style="top:117px"><p class="mini-name">Name of drink ...............12$</p><p class="mini-desc">Nulla tempus justo in nunc eleifend,<br>nec sagittis nunc imperdiet.</p></div>
      <div class="mini-item" style="top:148px"><p class="mini-name">Name of drink ...............11$</p><p class="mini-desc">Nulla tempus justo in nunc eleifend,<br>nec sagittis nunc imperdiet.</p></div>
    </div>
  </div>
  <div class="panel panel-white on-white" style="left:129px">
    <h3 class="abs center-x mini-head" style="top:11px">Frühstücksvariationen</h3>
    <div class="mini-icon" role="img" aria-label="Frühstücksteller, Strichzeichnung" style="top:26px;width:30px;margin-left:-15px"></div>
    <div class="mini-col" style="top:0;height:272px">
      <div class="mini-item" style="top:54px"><p class="mini-name">Name of dish................15$</p><p class="mini-desc">Nulla tempus justo in nunc eleifend,<br>nec sagittis nunc imperdiet.</p></div>
      <div class="mini-item" style="top:86px"><p class="mini-name">Name of dish................15$</p><p class="mini-desc">Nulla tempus justo in nunc eleifend,<br>nec sagittis nunc imperdiet.</p></div>
      <div class="mini-item" style="top:117px"><p class="mini-name">Name of dish................15$</p><p class="mini-desc">Nulla tempus justo in nunc eleifend,<br>nec sagittis nunc imperdiet.</p></div>
      <div class="mini-item" style="top:148px"><p class="mini-name">Name of dish................15$</p><p class="mini-desc">Nulla tempus justo in nunc eleifend,<br>nec sagittis nunc imperdiet.</p></div>
      <div class="mini-item" style="top:231px"><p class="mini-name">Name of dish................15$</p><p class="mini-desc">Nulla tempus justo in nunc eleifend,<br>nec sagittis nunc imperdiet.</p></div>
    </div>
    <div class="mini-rule" style="top:179px"></div>
    <h3 class="abs center-x mini-head" style="top:186px">Eierspeisen</h3>
    <div class="mini-icon" role="img" aria-label="Henne im Nest, Strichzeichnung" style="top:201px;width:24px;height:18px;margin-left:-12px"></div>
  </div>
  <div class="panel panel-dark on-dark" style="left:258px">
    <div class="mini-col" style="top:0;height:272px">
      <div class="mini-item" style="top:16px"><p class="mini-name">Name of dish...............15$</p><p class="mini-desc">Nulla tempus justo in nunc eleifend,<br>nec sagittis nunc imperdiet.</p></div>
      <div class="mini-item" style="top:48px"><p class="mini-name">Name of dish...............15$</p><p class="mini-desc">Nulla tempus justo in nunc eleifend,<br>nec sagittis nunc imperdiet.</p></div>
      <div class="mini-item" style="top:81px"><p class="mini-name">Name of dish...............15$</p><p class="mini-desc">Nulla tempus justo in nunc eleifend,<br>nec sagittis nunc imperdiet.</p></div>
      <div class="mini-item" style="top:167px"><p class="mini-name">Name of dish...............15$</p><p class="mini-desc">Nulla tempus justo in nunc eleifend,<br>nec sagittis nunc imperdiet.</p></div>
      <div class="mini-item" style="top:199px"><p class="mini-name">Name of dish...............15$</p><p class="mini-desc">Nulla tempus justo in nunc eleifend,<br>nec sagittis nunc imperdiet.</p></div>
      <div class="mini-item" style="top:232px"><p class="mini-name">Name of dish...............15$</p><p class="mini-desc">Nulla tempus justo in nunc eleifend,<br>nec sagittis nunc imperdiet.</p></div>
    </div>
    <div class="mini-rule" style="top:112px"></div>
    <h3 class="abs center-x mini-head" style="top:121px;color:var(--tan-text)">Frühstück zum löffeln</h3>
    <div class="mini-icon" role="img" aria-label="Schüssel mit Kanne, Strichzeichnung" style="top:135px;width:14px;height:18px;margin-left:-7px"></div>
  </div>
</section>

<!-- Kids menu cover -->
<section class="sheet kids-cover">
  <div class="brand-seal" style="left:25px;top:58px;width:86px;height:86px;font-size:13px">die Kurbel.</div>
  <p class="abs center-x page-title" style="top:161px;font-size:11.5px">Kids Menu</p>
  <div class="icon-slot" role="img" aria-label="Kind mit Kochmütze, Strichzeichnung" style="left:58px;top:187px;width:20px;height:26px;background:linear-gradient(135deg,#ffffff,#bdbdbd)"></div>
  <div class="icon-slot" role="img" aria-label="Pancake-Teller, Strichzeichnung" style="left:43px;top:222px;width:51px;height:16px;background:linear-gradient(135deg,#ffffff,#bdbdbd)"></div>
</section>

<!-- Kids menu inside -->
<section class="sheet kids-inside">
  <div class="abs" style="left:0;top:0;width:100%;height:38px;background:var(--ink)"></div>
  <h2 class="abs center-x page-title" style="top:12px;font-size:11.5px">Kids Menu</h2>
  <div class="abs on-white" style="left:0;top:38px;width:100%;height:137px">
    <h3 class="abs center-x mini-head" style="top:8px">Frühstück</h3>
    <div class="mini-icon" role="img" aria-label="Sandwich, Strichzeichnung" style="top:22px;width:24px;height:13px;margin-left:-12px"></div>
    <div class="mini-col" style="left:30px;top:0;height:137px">
      <div class="mini-item" style="top:41px"><p class="mini-name">Name of dish................15$</p><p class="mini-desc">Nulla tempus justo in nunc eleifend,<br>nec sagittis nunc imperdiet.</p></div>
      <div class="mini-item" style="top:73px"><p class="mini-name">Name of dish................15$</p><p class="mini-desc">Nulla tempus justo in nunc eleifend,<br>nec sagittis nunc imperdiet.</p></div>
      <div class="mini-item" style="top:105px"><p class="mini-name">Name of dish................15$</p><p class="mini-desc">Nulla tempus justo in nunc eleifend,<br>nec sagittis nunc imperdiet.</p></div>
    </div>
  </div>
  <div class="abs on-tan" style="left:0;top:175px;width:100%;height:116px;background:var(--tan)">
    <h3 class="abs center-x mini-head" style="top:11px">Pancakes</h3>
    <div class="mini-icon" role="img" aria-label="Pancake-Teller, Strichzeichnung" style="top:24px;width:34px;height:11px;margin-left:-17px"></div>
    <div class="mini-col" style="left:30px;top:0;height:116px">
      <div class="mini-item" style="top:47px"><p class="mini-name">Name of dish................15$</p><p class="mini-desc">Nulla tempus justo in nunc eleifend,<br>nec sagittis nunc imperdiet.</p></div>
      <div class="mini-item" style="top:79px"><p class="mini-name">Name of dish................ 9$</p><p class="mini-desc">Nulla tempus justo in nunc eleifend,<br>nec sagittis nunc imperdiet.</p></div>
    </div>
  </div>
</section>

</body>
</html>
```